Business Card for Bloom Vitality & Strength

Hi can you please design a business card with my logo and program logo (the new one I just sent) somewhere on it too maybe on the back? Needs to be eye catching and super cool.
Marla Quintby, Director
Master Personal Trainer & Nutrition Coach
0412 786 305
Www.bloomvitalitystrength.com.au
Insta (logo) bloom_vitality_strength #bloomyou7x72018

Target Market(s)

30+ women looking to change lifestyle to healthy mind body etc

Industry/Entity Type

Health And Wellness

Contact Information for Business Card

As above

Font styles to use
Sans Serif

Colors

Designer to choose colors to be used in the design.

Requirements
Must have
• Must super cool and edgy with a bit of cuteness

```html
<!DOCTYPE html>
<html lang="en">
<head>
<meta charset="utf-8">
<title>Bloom Vitality &amp; Strength – Business Card</title>
<link href="https://fonts.googleapis.com/css2?family=Oswald:wght@500&family=Roboto:wght@400;700&display=swap" rel="stylesheet">
<style>
  :root {
    --backdrop: #c6c6c6;
    --card: #f4f4f4;
    --ink: #161616;
    --red: #c10a12;
    --red-dark: #8e0a0f;
    --green: #1f9a5a;
    --white: #ffffff;
  }
  * { margin: 0; padding: 0; box-sizing: border-box; }
  html, body { width: 1200px; height: 576px; overflow: hidden; }
  body {
    background: var(--backdrop);
    font-family: "Roboto", Arial, sans-serif;
    color: var(--ink);
    position: relative;
  }
  .card {
    position: absolute;
    background: var(--card);
    border-radius: 12px;
    overflow: hidden;
    box-shadow: 0 3px 8px rgba(0,0,0,0.25);
  }
  .card--front { left: 82px; top: 138px; width: 484px; height: 294px; }
  .card--back  { left: 602px; top: 138px; width: 481px; height: 291px; }

  .brand {
    position: absolute;
    display: flex;
    align-items: center;
    gap: 12px;
  }
  .brand__dot { border-radius: 50%; background: var(--red); flex: none; }
  .brand__name {
    font-weight: 700;
    color: var(--ink);
    text-transform: uppercase;
    line-height: 1.05;
  }
  .card--front .brand { left: 0; right: 0; top: 108px; justify-content: center; }
  .card--front .brand__dot { width: 40px; height: 40px; }
  .card--front .brand__name { font-size: 32px; }

  .front-band {
    position: absolute; left: 0; right: 0; bottom: 0; height: 10px;
    background: linear-gradient(90deg, var(--red-dark), var(--red) 50%, var(--red-dark));
  }

  .card--back .brand { left: 22px; top: 82px; gap: 10px; }
  .card--back .brand__dot { width: 26px; height: 26px; }
  .card--back .brand__name { font-size: 23px; }

  .program {
    position: absolute; left: 24px; top: 178px;
    display: flex; align-items: center; gap: 7px;
  }
  .program__dot { width: 18px; height: 18px; border-radius: 50%; background: var(--red); }
  .program__name { font-size: 15px; font-weight: 700; color: var(--ink); }

  .person { position: absolute; right: 21px; top: 38px; text-align: right; }
  .person__name {
    font-family: "Oswald", "Arial Narrow", sans-serif;
    font-weight: 500; font-size: 20px; color: var(--red-dark); line-height: 1.2;
  }
  .person__role { font-size: 12px; line-height: 15px; margin-top: 4px; }

  .wave { position: absolute; left: 0; top: 0; width: 481px; height: 291px; }

  .contacts {
    position: absolute; right: 17px; top: 200px;
    list-style: none; text-align: right;
  }
  .contacts li {
    display: flex; justify-content: flex-end; align-items: center; gap: 9px;
    font-size: 12px; color: var(--white); height: 18.5px;
  }
  .contacts svg { width: 11px; height: 11px; flex: none; }
</style>
</head>
<body>

<section class="card card--front" aria-label="Card front">
  <div class="brand">
    <span class="brand__dot"></span>
    <span class="brand__name">Bloom Vitality &amp;<br>Strength</span>
  </div>
  <div class="front-band"></div>
</section>

<section class="card card--back" aria-label="Card back">
  <svg class="wave" viewBox="0 0 481 291" aria-hidden="true">
    <defs>
      <linearGradient id="redSweep" x1="0" y1="1" x2="1" y2="0">
        <stop offset="0" stop-color="#8e0a0f"/>
        <stop offset="0.5" stop-color="#d20d15"/>
        <stop offset="1" stop-color="#a50a10"/>
      </linearGradient>
    </defs>
    <path d="M0,226 C90,275 200,262 290,212 C360,172 420,150 481,156 V291 H0 Z" fill="url(#redSweep)"/>
    <path d="M0,222 C70,250 160,250 240,232 C160,264 60,264 0,250 Z" fill="var(--green)"/>
    <path d="M40,234 C120,244 190,222 260,188 C340,150 420,136 481,140 V147 C420,144 345,160 268,196 C195,230 120,248 40,234 Z" fill="var(--ink)"/>
  </svg>

  <div class="person">
    <p class="person__name">Marla Quintby, Director</p>
    <p class="person__role">Master Personal Trainer<br>&amp; Nutrition Coach</p>
  </div>

  <div class="brand">
    <span class="brand__dot"></span>
    <span class="brand__name">Bloom Vitality &amp;<br>Strength</span>
  </div>

  <div class="program">
    <span class="program__dot"></span>
    <span class="program__name">Bloom You 7x7</span>
  </div>

  <ul class="contacts">
    <li>0412 786 305
      <svg viewBox="0 0 12 12" aria-hidden="true"><path d="M2 1h2l1 3-1.5 1a7 7 0 0 0 3.5 3.5L8 7l3 1v2a1 1 0 0 1-1 1A9 9 0 0 1 1 2a1 1 0 0 1 1-1z" fill="#fff"/></svg></li>
    <li>bloomvitalitystrength.com.au
      <svg viewBox="0 0 12 12" aria-hidden="true"><rect x="0.5" y="2" width="11" height="8" fill="#fff"/><path d="M0.5 2l5.5 4.5L11.5 2" stroke="#b00" fill="none"/></svg></li>
    <li>marla@bloomvitalitystrength.com.au
      <svg viewBox="0 0 12 12" aria-hidden="true"><circle cx="6" cy="6" r="5" stroke="#fff" fill="none"/><ellipse cx="6" cy="6" rx="2.2" ry="5" stroke="#fff" fill="none"/><path d="M1 6h10" stroke="#fff"/></svg></li>
    <li>#bloom_vitality_strength, #bloomyou7x72018
      <svg viewBox="0 0 12 12" aria-hidden="true"><circle cx="6" cy="6" r="5.5" fill="#fff"/></svg></li>
  </ul>
</section>

</body>
</html>
```